Home Baker of cakes, muffins, cookies and pastries.

I am looking for business cards for my home baking business called " Zippy Pom-Pom Bakes " - I want them to be super cute and girly, yet simple and modern at the same time. Pastel colours is what I envision with the main colour being baby pink.

```html
<!DOCTYPE html>
<html lang="en">
<head>
<meta charset="utf-8">
<title>Zippy Pom-Pom Bakes — Business Cards</title>
<link rel="stylesheet" href="https://fonts.googleapis.com/css2?family=Raleway:wght@400;500&family=Great+Vibes&family=Open+Sans:wght@400;600&display=swap">
<style>
  :root {
    --backdrop: #3a3a37;
    --card-dark: #161616;
    --card-light: #ffffff;
    --baby-pink: #e07ab8;
    --soft-pink: #e9a3cf;
    --mauve: #a78a92;
    --mauve-text: #8f6f7c;
    --divider: #c9b3bc;
    --tagline-light: #d8c8d0;
  }
  * { box-sizing: border-box; margin: 0; padding: 0; }
  html, body { width: 1200px; height: 824px; overflow: hidden; }
  body { background: var(--backdrop); position: relative; font-family: "Raleway", sans-serif; }

  .card { position: absolute; width: 500px; height: 286px; border-radius: 3px; overflow: hidden; }

  .card--front {
    left: 60px; top: 60px;
    background: var(--card-dark);
    display: flex; flex-direction: column; align-items: center; justify-content: center;
    box-shadow: 0 3px 0 #0c0c0c, 0 6px 0 #101010, 0 9px 0 #0c0c0c;
    overflow: visible;
  }
  .card--back {
    left: 630px; top: 330px;
    background: var(--card-light);
    display: flex; align-items: center;
  }

  .brand { display: flex; align-items: center; gap: 10px; }
  .brand__dot { width: 16px; height: 16px; border-radius: 50%; background: var(--baby-pink); flex: none; }
  .brand__name {
    font-family: "Raleway", sans-serif; font-weight: 500;
    color: var(--baby-pink); font-size: 30px; white-space: nowrap;
  }
  .tagline { font-size: 13px; margin-top: 16px; letter-spacing: .2px; }
  .card--front .tagline { color: var(--soft-pink); }

  .back__brand { width: 280px; flex: none; display: flex; justify-content: center; padding: 0 14px; }
  .back__brand .brand { gap: 8px; }
  .back__brand .brand__name { font-size: 19px; }
  .back__brand .brand__dot { width: 11px; height: 11px; }
  .back__divider { width: 1px; height: 150px; background: var(--divider); flex: none; }
  .contact { padding-left: 22px; font-family: "Open Sans", sans-serif; color: var(--mauve-text); }
  .contact__name { font-family: "Great Vibes", cursive; color: var(--baby-pink); font-size: 38px; line-height: 1; white-space: nowrap; }
  .contact__title { font-weight: 600; font-size: 12px; letter-spacing: 2px; text-align: right; margin: 2px 0 14px; color: var(--mauve); }
  .contact__row { display: flex; align-items: center; gap: 9px; font-size: 13px; margin-bottom: 6px; white-space: nowrap; }
  .contact__row svg { width: 14px; height: 14px; fill: var(--mauve); flex: none; }

  .showcase {
    position: absolute; left: 40px; top: 560px; width: 440px;
    display: flex; flex-direction: column; align-items: center;
  }
  .showcase .brand__name { font-size: 32px; }
  .showcase .tagline { color: var(--tagline-light); font-size: 14px; margin-top: 22px; }
</style>
</head>
<body>

  <section class="card card--front">
    <div class="brand">
      <span class="brand__dot"></span>
      <span class="brand__name">Zippy Pom-Pom Bakes</span>
    </div>
    <p class="tagline">Home Baker of cakes, muffins, cookies and pastries</p>
  </section>

  <section class="card card--back">
    <div class="back__brand">
      <div class="brand">
        <span class="brand__dot"></span>
        <span class="brand__name">Zippy Pom-Pom Bakes</span>
      </div>
    </div>
    <div class="back__divider"></div>
    <div class="contact">
      <p class="contact__name">Your Name</p>
      <p class="contact__title">JOB TITLE</p>
      <p class="contact__row">
        <svg viewBox="0 0 16 16" aria-hidden="true"><path d="M1 6c0-2 3-3 7-3s7 1 7 3v1h-3.5V5.5h-7V7H1zM3 8h10l1 5H2zm5 1.5a1.5 1.5 0 100 3 1.5 1.5 0 000-3z"/></svg>
        000 000 0000
      </p>
      <p class="contact__row">
        <svg viewBox="0 0 16 16" aria-hidden="true"><path d="M1 3h14v10H1zm1.5 1.3V5l5.5 4 5.5-4v-.7L8 8.2z"/></svg>
        yourname@xyz.com
      </p>
      <p class="contact__row">
        <svg viewBox="0 0 16 16" aria-hidden="true"><path d="M8 1a5 5 0 00-5 5c0 4 5 9 5 9s5-5 5-9a5 5 0 00-5-5zm0 3a2 2 0 110 4 2 2 0 010-4z"/></svg>
        Your Address
      </p>
    </div>
  </section>

  <section class="showcase">
    <div class="brand">
      <span class="brand__dot"></span>
      <span class="brand__name">Zippy Pom-Pom Bakes</span>
    </div>
    <p class="tagline">Home Baker of cakes, muffins, cookies and pastries</p>
  </section>

</body>
</html>
```